Construction Company Website Design

I need a Website Design for a Construction Company. I have attached logo and business card design files (a.i) to match styles and text for the website. I will need design for 3 pages:
1. A Home page
2. A secondary page (will be different information pages)
3. A contact page with submision form
Website to look professional and match the 'theme' across all pages, using main colours / reverse colours as per design files. Must be clear it is a construction related website without being over the top. Happy for the construction related details (whether that be images/outlines/backgrounds etc to be fairly subtle and not overbearing on the contect of the pages. It will be the content that will be most important, not the images within.

Content has not yet been fully completed but attached is a site map. Each page will need a space for the insertion of the relevant heading and associated content for that particular page. Example can be used as per attached map. If it is preferable to have content completed for this to be a more succesful project please advise and I will complete and submit.

Target Market(s)

Clients for potential construction projects. These could be a range of people. All would be very professional, well educated and put a substantial expection on the quality of website provided.

Industry/Entity Type

Construction

Number of Pages Required

3 page

Font styles to use
Serif
Sans Serif
Other font styles liked:
• fonts preferable as per design files provided unless designer beleives a different font would suit better

Requirements
Must have
• Colour scheme to match logo and business card files provided. Fonts that match as per provided files. Pages must be consistent with the theme carrying across all pages. All pages must have contact details at the bottom of the page.
• Contents of page 1 - 'Home page': multiple tab options / logo link
• Contents of page 2 - 'Secondary page': Top and side navigation / area for information and/or images.
• Contents of page - 'Contact us page': Top and side navigation / Submission form / area for logos such as linkdin, facebook etc.
Nice to have
• Would be good to have a or some generic construction related images - outlines / shadows / effects etc. These might be background images or outlines related to the relevant industry and are consistent across the pages. Could be outlines of buildings, images of men with hardhats etc etc. Good to see colour scheme as per design files used
Should not have
• No pictures of houses. Generally no photos. If any imagery of people must not show faces/details.

```html
<!DOCTYPE html>
<html lang="en">
<head>
<meta charset="utf-8">
<title>Norvane Constructions</title>
<link href="https://fonts.googleapis.com/css2?family=Roboto:ital,wght@0,300;0,400;0,500;0,700;1,300;1,400&display=swap" rel="stylesheet">
<style>
:root{
  --blue:#29a9e6;
  --blue-dark:#1c8fd0;
  --navy:#27324d;
  --text:#3b4561;
  --muted:#8c94aa;
  --line:#dde2ec;
  --soft:#f4f6fb;
  --white:#ffffff;
  --footer-base:#1b2233;
}
*{box-sizing:border-box;margin:0;padding:0}
html,body{width:1200px;height:3056px;overflow:hidden}
body{font-family:"Roboto",Arial,sans-serif;color:var(--text);background:var(--white);position:relative}
a{color:inherit;text-decoration:none}
.wrap{position:relative;width:1098px;margin:0 auto}

/* Hero */
.hero{position:relative;height:544px}
.hero-photo{position:absolute;inset:0;background:linear-gradient(160deg,#5f7f86 0%,#3d5a58 35%,#2e4a44 60%,#4f6d74 100%)}
.hero-photo::after{content:"";position:absolute;inset:0;background:linear-gradient(180deg,rgba(40,70,90,.25),rgba(41,169,230,.15))}
.logo{position:absolute;left:0;top:18px;width:305px;height:62px;background:var(--blue);clip-path:polygon(0 0,100% 0,88% 100%,0 100%);display:flex;align-items:center;padding-left:18px;gap:12px}
.logo-mark{width:14px;height:14px;border-radius:50%;background:var(--white)}
.logo-name{color:var(--white);font-weight:500;font-size:17px;letter-spacing:1px;text-transform:uppercase}
.main-nav{position:absolute;top:40px;left:444px;display:flex;gap:38px}
.main-nav a{color:var(--white);font-size:13px;font-weight:500;letter-spacing:.3px}
.hero-phone{position:absolute;top:22px;right:48px;color:var(--white);font-size:14px;font-weight:500}
.quote-btn{position:absolute;top:55px;right:39px;width:141px;height:33px;border-radius:17px;background:var(--white);color:var(--blue-dark);font-size:13px;display:flex;align-items:center;justify-content:center}

/* Intro band */
.intro{height:169px;background:var(--blue);color:var(--white);text-align:center;padding-top:16px}
.intro h1{font-size:20px;font-weight:500;line-height:27px}
.intro p{font-size:12px;margin-top:6px}
.call-btn{margin:14px auto 0;width:171px;height:41px;border:2px solid var(--white);border-radius:21px;display:flex;align-items:center;justify-content:center;gap:10px;font-size:13px;font-weight:500}

/* Section heads */
.label{font-size:15px;color:var(--muted);font-weight:300}
.heading{font-size:32px;font-weight:400;color:var(--navy);margin-top:6px}
.lede{font-size:12px;line-height:22px;color:var(--muted);font-weight:300}

/* Services */
.services{height:676px;background:var(--soft);padding-top:36px}
.services .lede{margin-top:38px;width:360px}
.service-body{display:flex;margin-top:70px}
.service-tabs{width:297px;list-style:none}
.service-tabs li{height:72px;display:flex;align-items:center;gap:18px;padding-left:14px;font-size:13px;color:var(--muted);font-weight:300}
.service-tabs li.active{background:var(--white);height:82px;color:var(--blue-dark);font-weight:400;box-shadow:0 2px 10px rgba(40,60,100,.06)}
.tab-thumb{width:46px;height:46px;border-radius:50%}
.t1{background:linear-gradient(135deg,#6f8f8c,#3c5a57)}
.t2{background:linear-gradient(135deg,#8a97aa,#51607a)}
.t3{background:linear-gradient(135deg,#e5cf9b,#b18a4e)}
.t4{background:linear-gradient(135deg,#3d5f93,#c88a3a)}
.t5{background:linear-gradient(135deg,#e6c59a,#b98450)}
.service-detail{margin-left:66px;width:690px;padding-top:14px}
.service-detail h2{font-size:22px;font-weight:400;color:var(--navy)}
.service-detail p{font-size:12px;line-height:20px;color:var(--muted);font-weight:300;margin-top:20px}
.service-detail p + p{margin-top:14px}
.details-link{display:inline-block;margin-top:20px;font-size:13px;color:var(--blue-dark)}
.gallery{display:flex;gap:39px;margin-top:22px}
.gallery div{width:200px;height:106px}
.g1{background:linear-gradient(135deg,#5d7a66,#b9c6c5)}
.g2{background:linear-gradient(135deg,#3e5a45,#8fa39a)}
.g3{background:linear-gradient(135deg,#9cb9c9,#4f6b63)}

/* Testimonials */
.testimonials{height:530px;text-align:center;padding-top:22px}
.testimonials .heading{margin-top:4px}
.testimonials .lede{width:440px;margin:30px auto 0;line-height:22px}
.quotes{position:relative;display:grid;grid-template-columns:1fr 1fr;margin-top:42px}
.quotes::before{content:"";position:absolute;left:0;right:0;top:104px;border-top:2px dotted #8cc9ec}
.quotes::after{content:"";position:absolute;left:548px;top:0;bottom:0;border-left:2px dotted #8cc9ec}
.quote{display:flex;align-items:center;gap:20px;height:104px}
.quote:nth-child(n+3){height:130px;padding-top:20px}
.quote.left{justify-content:flex-end;padding-right:36px;text-align:right}
.quote.right{padding-left:36px;text-align:left}
.quote blockquote{width:400px;font-style:italic;font-size:12px;line-height:18px;color:var(--muted);font-weight:300}
.quote cite{display:block;margin-top:8px;font-style:normal;font-size:12px;color:var(--navy);font-weight:400}
.avatar{flex:none;width:80px;height:80px;border-radius:50%;background:linear-gradient(135deg,#d9dde6,#9aa3b5);border:5px solid var(--white);box-shadow:0 2px 10px rgba(40,60,100,.15)}

/* News */
.news{height:607px;background:var(--soft);padding-top:28px}
.news .heading{margin-top:4px}
.news .lede{width:500px;margin-top:24px}
.cards{display:flex;gap:26px;margin-top:52px}
.card{width:256px;height:355px;background:var(--white);position:relative}
.card-photo{height:190px}
.c1{background:linear-gradient(135deg,#2f3d55,#7a4a2a)}
.c2{background:linear-gradient(135deg,#e6e2da,#5a3b25)}
.c3{background:linear-gradient(135deg,#8c4e34,#e9e3d8)}
.c4{background:linear-gradient(135deg,#d8cbb5,#6d4a33)}
.card h3{font-size:18px;font-weight:700;color:var(--navy);padding:18px 18px 0}
.card p{font-size:12px;line-height:17px;color:var(--muted);font-weight:300;padding:8px 18px 0}
.card-meta{position:absolute;left:18px;right:18px;bottom:14px;padding-top:14px;border-top:1px solid var(--line);display:flex;justify-content:space-between;font-size:11px;color:var(--text)}
.card-meta span{display:flex;align-items:center;gap:6px}

/* Contact */
.contact{height:367px;padding-top:44px}
.contact-grid{display:flex;gap:30px}
.contact h4{font-size:17px;font-weight:400;color:var(--navy)}
.mail-form{width:254px}
.field{border:1px solid var(--line);height:33px;font-size:11px;color:var(--muted);padding:0 10px;display:flex;align-items:center;border-radius:2px;font-weight:300}
.field-row{display:flex;gap:18px;margin-top:24px}
.field-row .field{flex:1}
.mail-form .field.full{margin-top:16px}
.mail-form .field.msg{height:70px;align-items:flex-start;padding-top:10px;margin-top:20px}
.send-btn{margin-top:20px;width:139px;height:33px;border-radius:17px;background:var(--blue);color:var(--white);font-size:12px;font-weight:500;display:flex;align-items:center;justify-content:center;letter-spacing:.3px}
.hq{width:534px;text-align:center}
.hq h4{margin-top:6px}
.hq-map{margin-top:24px;height:227px;background:linear-gradient(135deg,#e8eef2 0%,#c7e3f0 45%,#a9d4ec 60%,#e4ead9 100%)}
.info{width:234px}
.info p{font-size:12px;line-height:20px;color:var(--muted);font-weight:300;margin-top:18px}
.info p + p{margin-top:12px}
.info h4.follow{margin-top:16px}
.socials{display:flex;gap:10px;margin-top:18px}
.socials span{width:28px;height:28px;border-radius:50%;background:var(--blue)}

/* Footer */
.site-footer{position:absolute;left:0;top:2893px;width:1200px;height:142px;background:var(--blue);color:var(--white)}
.foot-logo{position:absolute;right:0;top:16px;width:253px;height:61px;background:var(--white);clip-path:polygon(12% 0,100% 0,100% 100%,0 100%);display:flex;align-items:center;justify-content:flex-end;padding-right:26px;gap:10px}
.foot-logo .logo-mark{background:var(--blue-dark);width:12px;height:12px}
.foot-logo .logo-name{color:var(--navy);font-size:13px}
.foot-nav{position:absolute;left:51px;top:46px;display:flex;align-items:center;gap:26px;font-size:13px;font-weight:500}
.foot-rule{position:absolute;left:51px;right:0;top:77px;border-top:1px solid rgba(255,255,255,.35)}
.foot-links{position:absolute;left:51px;top:95px;display:flex;gap:20px;font-size:11px}
.foot-legal{position:absolute;right:51px;top:95px;display:flex;gap:20px;font-size:11px}
.base-strip{position:absolute;left:0;top:3035px;width:1200px;height:21px;background:var(--footer-base)}
</style>
</head>
<body>

<header class="hero">
  <div class="hero-photo" role="img" aria-label="Aerial view of modern apartment blocks surrounded by pine forest"></div>
  <a class="logo" href="#"><span class="logo-mark"></span><span class="logo-name">Norvane Constructions</span></a>
  <nav class="main-nav"><a href="#">SERVICES</a><a href="#">OUR PROJECTS</a><a href="#">CULTURE</a></nav>
  <div class="hero-phone">+1 (800) 555 01 27</div>
  <a class="quote-btn" href="#">Request a Quote</a>
</header>

<section class="intro">
  <h1>Norvane Constructions is all about Building. In our part of the Construction<br>Maintenance, that usually means bringing best advancements to an Construction Building</h1>
  <p>See some of the features below and learn why businesses trust Norvane Constructions</p>
  <a class="call-btn" href="#">
    <svg width="12" height="12" viewBox="0 0 24 24"><path fill="#fff" d="M6.6 10.8a15.1 15.1 0 0 0 6.6 6.6l2.2-2.2a1 1 0 0 1 1-.25 11.4 11.4 0 0 0 3.6.57 1 1 0 0 1 1 1V20a1 1 0 0 1-1 1A17 17 0 0 1 3 4a1 1 0 0 1 1-1h3.5a1 1 0 0 1 1 1c0 1.25.2 2.45.57 3.57a1 1 0 0 1-.25 1z"/></svg>
    +1 (800) 555 01 27
  </a>
</section>

<section class="services">
  <div class="wrap">
    <div class="label">Services</div>
    <h2 class="heading">What we do ?</h2>
    <p class="lede">Sed ut perspiciatis unde omnis iste natus error sit voluptatem Neque porro quisquam est, qui dolorem ipsum quia dolor</p>
    <div class="service-body">
      <ul class="service-tabs">
        <li class="active"><span class="tab-thumb t1" role="img" aria-label="Commercial building thumbnail"></span>Commercial</li>
        <li><span class="tab-thumb t2" role="img" aria-label="Residential building thumbnail"></span>Residential</li>
        <li><span class="tab-thumb t3" role="img" aria-label="Building maintenance worker thumbnail"></span>Building Maintenance</li>
        <li><span class="tab-thumb t4" role="img" aria-label="Project management thumbnail"></span>Project Management</li>
        <li><span class="tab-thumb t5" role="img" aria-label="Renovation work thumbnail"></span>Renovations</li>
      </ul>
      <div class="service-detail">
        <h2>Commercial Services</h2>
        <p>Sed ut perspiciatis unde omnis iste natus error sit voluptatem accusantium doloremque laudantium, totam rem aperiam, eaque ipsa quae ab illo inventore veritatis et quasi architecto beatae vitae dicta sunt explicabo. Nemo enim ipsam voluptatem quia voluptas sit aspernatur aut odit aut fugit, sed quia consequuntur magni dolores eos qui.</p>
        <p>Sed ut perspiciatis unde omnis iste natus error sit voluptatem accusantium doloremque laudantium, totam rem aperiam, eaque ipsa quae ab illo inventore veritatis et quasi</p>
        <a class="details-link" href="#">Details &rsaquo;</a>
        <div class="gallery">
          <div class="g1" role="img" aria-label="Residential blocks among trees"></div>
          <div class="g2" role="img" aria-label="Glass building in a forest setting"></div>
          <div class="g3" role="img" aria-label="White apartment building exterior"></div>
        </div>
      </div>
    </div>
  </div>
</section>

<section class="testimonials">
  <div class="wrap">
    <div class="label">Testimonials</div>
    <h2 class="heading">What Our Client Says ?</h2>
    <p class="lede">What our clients say about our services and how we helped us and make them life better than before</p>
    <div class="quotes">
      <div class="quote left">
        <blockquote>Duis aute irure dolor in reprehenderit in voluptate velit esse cillum dolore eu fugiat nulla pariatur. Excepteur sint occaecat cupidatat non proident, sunt in culpa qui officia deserunt mollit.<cite>Evan Marsh, Operations Manager</cite></blockquote>
        <span class="avatar" role="img" aria-label="Client portrait"></span>
      </div>
      <div class="quote right">
        <span class="avatar" role="img" aria-label="Client portrait"></span>
        <blockquote>Provident, similique sunt in culpa qui officia deserunt mollitia animi, id est laborum et dolorum fuga. Et harum quidem rerum facilis est et expedita distinctio. Nam libero tempore, cum soluta nobis.<cite>Nora Bell, Creative Designer</cite></blockquote>
      </div>
      <div class="quote left">
        <blockquote>Luis aute irure dolor in reprehenderit in pluptate velit esse cillum dolore eu fugiat nulla pariatur. Excepteur sint occaecat cupidatat non proident, sunt in culpa qui officia deserunt mollit.<cite>Ruth Alden, Manager</cite></blockquote>
        <span class="avatar" role="img" aria-label="Client portrait"></span>
      </div>
      <div class="quote right">
        <span class="avatar" role="img" aria-label="Client portrait"></span>
        <blockquote>At vero eos et accusamus et iusto odio dignissimos ducimus qui blanditiis praesentium voluptatum deleniti atque corrupti quos dolores et quas molestias excepturi sint occaecati asperiores.<cite>Owen Pike, Developer</cite></blockquote>
      </div>
    </div>
  </div>
</section>

<section class="news">
  <div class="wrap">
    <div class="label">Media</div>
    <h2 class="heading">Latest News &amp; Views</h2>
    <p class="lede">Neque porro quisquam est, qui dolorem ipsum quia dolor sit amet, consectetur, adipisci velit, sed quia non</p>
    <div class="cards">
      <article class="card">
        <div class="card-photo c1" role="img" aria-label="Traveller walking with a leather bag"></div>
        <h3>Standard Post</h3>
        <p>Enim congue blandit. Lorem ipsum dolor sit amet, consectetur adipiscing elit. Quisque...</p>
        <div class="card-meta"><span><svg width="11" height="11" viewBox="0 0 24 24"><path fill="#3b4561" d="M5 4h2V2h2v2h6V2h2v2h2a1 1 0 0 1 1 1v15a1 1 0 0 1-1 1H5a1 1 0 0 1-1-1V5a1 1 0 0 1 1-1zm0 6v10h14V10z"/></svg>22 June, 2015</span><span><svg width="12" height="11" viewBox="0 0 24 22"><path fill="#3b4561" d="M12 1C5.9 1 1 4.8 1 9.5c0 2.4 1.3 4.6 3.4 6.1L3 21l5.4-3c1.1.3 2.3.5 3.6.5 6.1 0 11-3.8 11-8.5S18.1 1 12 1z"/></svg>0</span></div>
      </article>
      <article class="card">
        <div class="card-photo c2" role="img" aria-label="Glass coffee brewer on a table"></div>
        <h3>Video Post</h3>
        <p>Ultrices posuere cubilia curae curabitur sit amet tortor ut massa commodo. Vestibulum...</p>
        <div class="card-meta"><span><svg width="11" height="11" viewBox="0 0 24 24"><path fill="#3b4561" d="M5 4h2V2h2v2h6V2h2v2h2a1 1 0 0 1 1 1v15a1 1 0 0 1-1 1H5a1 1 0 0 1-1-1V5a1 1 0 0 1 1-1zm0 6v10h14V10z"/></svg>22 June, 2015</span><span><svg width="12" height="11" viewBox="0 0 24 22"><path fill="#3b4561" d="M12 1C5.9 1 1 4.8 1 9.5c0 2.4 1.3 4.6 3.4 6.1L3 21l5.4-3c1.1.3 2.3.5 3.6.5 6.1 0 11-3.8 11-8.5S18.1 1 12 1z"/></svg>0</span></div>
      </article>
      <article class="card">
        <div class="card-photo c3" role="img" aria-label="Café table against a brick wall"></div>
        <h3>Post with Image</h3>
        <p>Enim congue blandit. Lorem ipsum dolor sit amet, consectetur adipiscing elit. Quisque...</p>
        <div class="card-meta"><span><svg width="11" height="11" viewBox="0 0 24 24"><path fill="#3b4561" d="M5 4h2V2h2v2h6V2h2v2h2a1 1 0 0 1 1 1v15a1 1 0 0 1-1 1H5a1 1 0 0 1-1-1V5a1 1 0 0 1 1-1zm0 6v10h14V10z"/></svg>22 June, 2015</span><span><svg width="12" height="11" viewBox="0 0 24 22"><path fill="#3b4561" d="M12 1C5.9 1 1 4.8 1 9.5c0 2.4 1.3 4.6 3.4 6.1L3 21l5.4-3c1.1.3 2.3.5 3.6.5 6.1 0 11-3.8 11-8.5S18.1 1 12 1z"/></svg>0</span></div>
      </article>
      <article class="card">
        <div class="card-photo c4" role="img" aria-label="Leather wallet on a patterned surface"></div>
        <h3>Image Post</h3>
        <p>Ultrices posuere cubilia curae curabitur sit amet tortor ut massa commodo. Vestibulum...</p>
        <div class="card-meta"><span><svg width="11" height="11" viewBox="0 0 24 24"><path fill="#3b4561" d="M5 4h2V2h2v2h6V2h2v2h2a1 1 0 0 1 1 1v15a1 1 0 0 1-1 1H5a1 1 0 0 1-1-1V5a1 1 0 0 1 1-1zm0 6v10h14V10z"/></svg>22 June, 2015</span><span><svg width="12" height="11" viewBox="0 0 24 22"><path fill="#3b4561" d="M12 1C5.9 1 1 4.8 1 9.5c0 2.4 1.3 4.6 3.4 6.1L3 21l5.4-3c1.1.3 2.3.5 3.6.5 6.1 0 11-3.8 11-8.5S18.1 1 12 1z"/></svg>3</span></div>
      </article>
    </div>
  </div>
</section>

<section class="contact">
  <div class="wrap contact-grid">
    <form class="mail-form">
      <h4>Feel Free to Mail</h4>
      <div class="field-row"><div class="field">Name *</div><div class="field">Email *</div></div>
      <div class="field full">Subject</div>
      <div class="field msg">Write Your Message Here...</div>
      <div class="send-btn">SEND MESSAGE</div>
    </form>
    <div class="hq">
      <h4>Headquarters</h4>
      <div class="hq-map" role="img" aria-label="Street map showing the headquarters location by the harbour"></div>
    </div>
    <div class="info">
      <h4>Contact Info</h4>
      <p>Our staff is available to you from 9AM until 5PM on weekdays.</p>
      <p>Phone: +1 (33) 555 0192<br>Office: Harbor Point Plaza<br>Email: hello@norvanebuild.com</p>
      <h4 class="follow">Follow Us on</h4>
      <div class="socials"><span></span><span></span><span></span><span></span><span></span></div>
    </div>
  </div>
</section>

<footer class="site-footer">
  <div class="foot-logo"><span class="logo-mark"></span><span class="logo-name">Norvane Constructions</span></div>
  <nav class="foot-nav">
    <svg width="14" height="14" viewBox="0 0 24 24"><circle cx="10" cy="10" r="6.5" fill="none" stroke="#fff" stroke-width="3"/><path d="M15 15l6 6" stroke="#fff" stroke-width="3" stroke-linecap="round"/></svg>
    <a href="#">Help &amp; Contact</a><a href="#">Services</a><a href="#">Our Projects</a><a href="#">Request a Quote</a>
  </nav>
  <div class="foot-rule"></div>
  <nav class="foot-links"><a href="#">About</a><a href="#">News</a><a href="#">Careers</a><a href="#">Public Policy</a><a href="#">Culture</a><a href="#">People</a><a href="#">Partners</a></nav>
  <div class="foot-legal"><span>&copy; 2006 - 2016</span><a href="#">Privacy</a><a href="#">Legal</a><a href="#">Feedback</a></div>
</footer>
<div class="base-strip"></div>

</body>
</html>
```